Design some Business Cards

Hi, I would like some business cards designed with a logo.
Typical size ultimately for cards at 300dpi.
Text to include:
Logo: Open to interpretation
Name: Sugar Petal Vossberg
Mob: 0481907 846.............. (To advise on winner)
Email: sweetpetalv@.......(To advise on winner)
Singer, Songwriter, Actress, Entertainer Extraordinaire

Yes, she is a singer!! Open to any design that jumps out and is fresh. Loves the colour pink. Is partial to anime. She is a stylistic down to earth Diva. ! Fierce, Fabulous and infamous.!!

Look forrwrd to seeing and chatting with to choose work in 7 days, or award sooner.

Cheers!

```html
<!DOCTYPE html>
<html lang="en">
<head>
<meta charset="utf-8">
<title>Sugar Petal Vossberg – Business Cards</title>
<link rel="stylesheet" href="https://fonts.googleapis.com/css2?family=Merienda:wght@400;700&display=swap">
<style>
  :root {
    --backdrop: #1b1b1d;
    --card-pink: #dd3a7f;
    --splash-pink: rgba(240, 40, 105, 0.75);
    --splash-coral: rgba(245, 100, 100, 0.6);
    --splash-lilac: rgba(245, 110, 185, 0.45);
    --band-white: #ffffff;
    --ink-pink: #d0306f;
  }
  * { box-sizing: border-box; margin: 0; padding: 0; }
  html, body {
    width: 1200px; height: 900px; overflow: hidden;
    background: var(--backdrop);
  }
  .stage {
    position: relative; width: 1200px; height: 900px;
    display: flex; align-items: center; justify-content: center; gap: 90px;
  }
  .card {
    position: relative; width: 400px; height: 560px;
    background: var(--card-pink);
    border-radius: 26px; overflow: hidden;
    font-family: "Merienda", cursive;
    color: var(--ink-pink);
  }
  .card__splash {
    position: absolute; inset: 0;
    background:
      radial-gradient(90px 80px at 45% 22%, var(--splash-pink), transparent),
      radial-gradient(75px 65px at 68% 42%, var(--splash-coral), transparent),
      radial-gradient(70px 60px at 22% 36%, var(--splash-lilac), transparent),
      radial-gradient(55px 45px at 55% 62%, var(--splash-coral), transparent);
  }
  .card__band {
    position: absolute; left: -100px; width: 620px; height: 72px;
    background: var(--band-white);
    transform: rotate(-22deg);
    display: flex; flex-direction: column; align-items: center; justify-content: center;
    text-align: center;
  }
  .card--front .card__band { top: 200px; }
  .card--back .card__band { top: 330px; height: 60px; }
  .name { font-size: 24px; font-weight: 700; letter-spacing: 1px; }
  .roles { font-size: 11px; font-weight: 700; margin-top: 2px; }
  .website { font-size: 15px; }
  .contact-box {
    position: absolute; right: 0; bottom: 0; width: 260px; height: 240px;
    background: var(--band-white);
    border-radius: 26px 0 26px 0;
    padding: 34px 16px 0 24px;
    font-size: 14px; line-height: 1.35;
  }
  .contact-box p { margin-bottom: 18px; white-space: nowrap; }
</style>
</head>
<body>
<main class="stage">
  <section class="card card--front">
    <div class="card__splash" role="img" aria-label="Pink paint splatter decoration"></div>
    <div class="card__band">
      <h1 class="name">Sugar Petal Vossberg</h1>
      <p class="roles">Singer, Songwriter, Actress, Entertainer Extraordinaire</p>
    </div>
    <div class="contact-box">
      <p class="phone">0481907 846</p>
      <p class="email">sweetpetalv@petalmail.com</p>
      <p class="address">57/2 lane<br>orivale, Australia</p>
    </div>
  </section>
  <section class="card card--back">
    <div class="card__splash" role="img" aria-label="Pink paint splatter decoration"></div>
    <div class="card__band">
      <p class="website">www. Sugar Petal Vossberg.com</p>
    </div>
  </section>
</main>
</body>
</html>
```